Business Card Design

Hi,

Just upload registered body logos

On the back of the card i would like the registered body logos as per the footer of our letter head.

also if space an arae for the services we provide

Target Market(s)

Commercial & Domestic property owners landlords

Industry/Entity Type

Business

Contact Information for Business Card

Fenwillow Estate & Repair Services Ltd

Tel: 01874 358 926
Email: info@fenwillow-ltd.example
www.fenwillow-ltd.example

Company Reg. No.(England) 7341968. VAT No. 413 2857 60

Owen Tasker

Unit 9
Millvane Business Park
Corley Lane
Brackenford
Westmere
SO47 8PN

Requirements
Must have
• Company logo as attached design – maybe with a SLIGHT revamp
Nice to have
• Two / three colours
Should not have
• Clipart ‘cartoon style’ artwork

```html
<!DOCTYPE html>
<html lang="en">
<head>
<meta charset="utf-8">
<title>Fenwillow Estate &amp; Repair Services Ltd – Business Card</title>
<link rel="stylesheet" href="https://fonts.googleapis.com/css2?family=Open+Sans:wght@400;600;700&display=swap">
<style>
  :root {
    --backdrop: #e2e2e2;
    --card-dark: #0b0b0b;
    --card-light: #f7f7f7;
    --brand-red: #c8163a;
    --ink: #2b2b2b;
    --white: #ffffff;
  }
  * { margin: 0; padding: 0; box-sizing: border-box; }
  html, body {
    width: 1200px; height: 900px; overflow: hidden;
    background: var(--backdrop);
    font-family: "Open Sans", Arial, sans-serif;
  }
  .stage {
    position: relative; width: 1200px; height: 900px;
    display: flex; align-items: center; justify-content: center; gap: 60px;
  }
  .card {
    position: relative; width: 510px; height: 330px;
    box-shadow: 0 6px 18px rgba(0,0,0,0.18);
    overflow: hidden;
  }

  /* Front */
  .card--front { background: var(--card-dark); }
  .front-brand {
    position: absolute; left: 0; right: 0; top: 108px;
    display: flex; align-items: center; justify-content: center; gap: 14px;
  }
  .brand-mark { width: 18px; height: 18px; background: var(--brand-red); }
  .front-brand .brand-name {
    color: var(--white); font-weight: 700; font-size: 58px; letter-spacing: -1px; line-height: 1;
  }
  .front-web {
    position: absolute; left: 0; right: 0; top: 222px; text-align: center;
    color: var(--brand-red); font-size: 15px; letter-spacing: 2.5px;
  }

  /* Back */
  .card--back { background: var(--card-light); }
  .back-details { position: absolute; left: 38px; top: 34px; color: var(--ink); font-size: 12px; line-height: 1.45; }
  .company-name { color: var(--brand-red); font-weight: 700; font-size: 15px; margin-bottom: 14px; }
  .contact-label { color: var(--brand-red); }
  .contact-web { color: var(--brand-red); }
  .detail-group { margin-bottom: 12px; }
  .back-brand {
    position: absolute; right: 38px; bottom: 52px;
    display: flex; align-items: center; gap: 10px;
  }
  .back-brand .brand-mark { width: 12px; height: 12px; }
  .back-brand .brand-name { color: var(--brand-red); font-weight: 700; font-size: 36px; letter-spacing: -0.5px; line-height: 1; }
  .back-band { position: absolute; left: 0; right: 0; bottom: 0; height: 24px; background: var(--brand-red); }
</style>
</head>
<body>
  <main class="stage">
    <section class="card card--front" aria-label="Business card front">
      <div class="front-brand">
        <span class="brand-mark"></span>
        <span class="brand-name">Fenwillow</span>
      </div>
      <p class="front-web">www.fenwillow-ltd.example</p>
    </section>

    <section class="card card--back" aria-label="Business card back">
      <div class="back-details">
        <p class="company-name">Fenwillow Estate &amp; Repair Services Ltd</p>
        <div class="detail-group">
          <p><span class="contact-label">T:</span> 01874 358 926</p>
          <p><span class="contact-label">E:</span> info@fenwillow-ltd.example</p>
          <p class="contact-web">www.fenwillow-ltd.example</p>
        </div>
        <div class="detail-group">
          <p>Company Reg. No. (England) 7341968.</p>
          <p>VAT No. 413 2857 60</p>
        </div>
        <div class="detail-group">
          <p>Owen Tasker Unit 9</p>
          <p>Millvane Business Park Corley Lane</p>
          <p>Brackenford Westmere SO47 8PN</p>
        </div>
      </div>
      <div class="back-brand">
        <span class="brand-mark"></span>
        <span class="brand-name">Fenwillow</span>
      </div>
      <div class="back-band"></div>
    </section>
  </main>
</body>
</html>
```